Law Firm Website

We are looking to update our old, tired and very flat website. We have someone who will code and host the site but we need some design inspiration. The website will consist of no more than 2/3 pages, possibly with pop-ups for information. We already have all the blurb. We would like something distinctive, clean and eye-catching, using the purple and white theme that we already use on our firm stationery. Examples uploaded. Current website URL is www.dunmorewillett.example.

Industry/Entity Type

Law Firm

```html
<!DOCTYPE html>
<html lang="en">
<head>
<meta charset="utf-8">
<title>Contact Us – Dunmore + Willett</title>
<link rel="stylesheet" href="https://fonts.googleapis.com/css2?family=Tinos:wght@400;700&display=swap">
<style>
  :root {
    --purple: #5e4a85;
    --purple-text: #5c4a86;
    --black: #000000;
    --white: #ffffff;
    --soft-white: #e8e6ee;
    --field-border: #d9d9d9;
  }
  * { box-sizing: border-box; margin: 0; padding: 0; }
  html, body { width: 1200px; height: 1123px; overflow: hidden; background: var(--black); }
  body { position: relative; font-family: "Tinos", "Times New Roman", serif; color: var(--soft-white); }

  .site-header { position: absolute; left: 0; top: 0; width: 1200px; height: 353px; background: var(--purple); }
  .partner-card { position: absolute; font-size: 17px; line-height: 22.5px; color: var(--soft-white); font-style: normal; }
  .partner-card .partner-name { font-size: 20px; line-height: 26px; }
  .partner-card .phone-lines { margin-top: 22px; }
  .partner-left { left: 62px; top: 52px; }
  .partner-right { left: 972px; top: 65px; }

  .firm-name {
    position: absolute; left: 230px; top: 84px; width: 720px;
    text-align: center;
    font-family: "Tinos", "Times New Roman", serif;
    font-size: 60px; font-weight: 400; line-height: 70px; color: var(--white);
  }

  .main-nav { position: absolute; left: 0; top: 325px; width: 1200px; height: 28px; font-size: 22px; color: var(--soft-white); }
  .main-nav a { position: absolute; color: inherit; text-decoration: none; white-space: nowrap; }

  .page-title { position: absolute; left: 40px; top: 418px; font-size: 26px; font-weight: 700; color: var(--purple-text); }

  .field-label { position: absolute; font-size: 22px; line-height: 22px; color: var(--soft-white); }
  .field-box { position: absolute; width: 376px; height: 29px; border: 2px solid var(--field-border); background: var(--black); }
  .field-box.enquiry { height: 131px; }

  .send-button {
    position: absolute; left: 538px; top: 893px; width: 138px; height: 38px;
    border: 2px solid var(--field-border); background: var(--black);
    font-family: "Tinos", "Times New Roman", serif; font-size: 21px; color: var(--soft-white);
  }

  .footer-name {
    position: absolute; left: 0; top: 1032px; width: 1200px; text-align: center;
    font-size: 36px; color: var(--purple-text);
  }
</style>
</head>
<body>
  <header class="site-header">
    <address class="partner-card partner-left">
      <div class="partner-name">Daniel Dunmore</div>
      <div>12b Larkfield Row</div>
      <div>Hillmere</div>
      <div>London NW9 4QT</div>
      <div class="phone-lines">
        <div>Tel: 0333 900 0146</div>
        <div>Fax: 020 7946 0321</div>
      </div>
    </address>

    <div class="firm-name">Dunmore + Willett</div>

    <address class="partner-card partner-right">
      <div class="partner-name">Peter Willett</div>
      <div>41C Orchard Way</div>
      <div>Fernbrook</div>
      <div>Hertfordshire AL9 2XY</div>
      <div class="phone-lines">
        <div>Tel: 0845 0146382</div>
        <div>Fax: 020 7946 0587</div>
      </div>
    </address>

    <nav class="main-nav">
      <a href="#" style="left:146px">home</a>
      <a href="#" style="left:348px">area of experties</a>
      <a href="#" style="left:588px">daniel dunmore + peter willett</a>
      <a href="#" style="left:955px">contact</a>
    </nav>
  </header>

  <main>
    <h1 class="page-title">Contact Us</h1>

    <form class="contact-form">
      <label class="field-label" style="left:49px;top:508px">First Name:</label>
      <div class="field-box" style="left:193px;top:504px"></div>

      <label class="field-label" style="left:49px;top:598px">Last Name:</label>
      <div class="field-box" style="left:193px;top:594px"></div>

      <label class="field-label" style="left:49px;top:688px">Company:<br>(Optional)</label>
      <div class="field-box" style="left:193px;top:686px"></div>

      <label class="field-label" style="left:659px;top:508px">Email:</label>
      <div class="field-box" style="left:790px;top:504px"></div>

      <label class="field-label" style="left:659px;top:598px">Telephone:<br>(Optional)</label>
      <div class="field-box" style="left:790px;top:591px"></div>

      <label class="field-label" style="left:659px;top:710px">Enquiry:</label>
      <div class="field-box enquiry" style="left:790px;top:675px"></div>

      <button class="send-button" type="button">send enquiry</button>
    </form>
  </main>

  <footer>
    <div class="footer-name">Dunmore &amp; Willett</div>
  </footer>
</body>
</html>
```